Make a website for Velmora, a Luxury and Modern Concierge Platform based in the UAE

Concierge Platform that has various luxury and exotic actives available to clients, itinerary planning for a dubai / uae based holiday.
Want the website to appear luxury, modern and easy to understand, with a landing page that can captivate customers, majority will use Mobile but Desktop should look good too. Chatline Contact pop-out, and email sign up list. Social Link (Circlefeed, Snapgrid, Chatline, Chatline Broadcast, Twitter/X, etc).
Ability to make it Dark and Light themed.
Second page Page that has a list of activities on a drop down/ list, as follows:
Flights
Car Rental
Luxury Car Rental
Chauffer
Yachts/ Boats
Jet Ski / Watersports
Buggies/ ATV
Dining
Tickets/Events
Apartments/ Hotels
Personal Shopping.
Link to competitors, who's websites appear basic and could be 100% improved, for examples:
- https://www.quietharbourstays.example/
- https://www.tivra.example/
- https://www.gulf-latch.example/
- https://thelomarenhouse.example/dubai.html
- https://www.theplatinumhostdesk.example/concierge-service-dubai/
Open to logo designs, we own Velmora.com.
Colours:
Luxury Style, Black and Gold is often used, but maybe over-used?
A modern colour palette White, Light Blue, Light Grey, but we aren't experts at this, so this isn't by any means strict criteria, let the creative mind run free.
Thank you

```html
<!DOCTYPE html>
<html lang="en">
<head>
<meta charset="UTF-8">
<title>Velmora — Contact</title>
<link href="https://fonts.googleapis.com/css2?family=Anton&family=Bebas+Neue&family=Oswald:wght@300;400&display=swap" rel="stylesheet">
<style>
  :root {
    --sand: #c29266;
    --espresso: #1c100a;
    --ink: #000000;
    --field: #ffffff;
    --placeholder: #6b6b6b;
  }
  * { margin: 0; padding: 0; box-sizing: border-box; }
  html, body { width: 702px; height: 1200px; overflow: hidden; background: var(--espresso); }
  .page { position: relative; width: 702px; height: 1200px; }

  .signup-band {
    position: absolute; left: 0; top: 0; width: 702px; height: 351px;
    background: var(--sand); text-align: center;
  }
  .signup-title {
    position: absolute; left: 0; right: 0; top: 22px;
    font-family: "Anton", sans-serif; font-weight: 400; font-size: 41px; line-height: 52px;
    color: var(--ink);
  }
  .email-field {
    position: absolute; left: 70px; top: 83px; width: 562px; height: 45px;
    background: var(--field); border-radius: 3px;
    padding-left: 24px; font-family: Arial, sans-serif; font-size: 17px; color: var(--placeholder);
    display: flex; align-items: center;
  }
  .join-button {
    position: absolute; left: 288px; top: 142px; width: 126px; height: 41px;
    background: var(--espresso); border-radius: 2px;
    color: var(--sand); font-family: "Oswald", sans-serif; font-size: 10px; letter-spacing: 1px;
    display: flex; align-items: center; justify-content: center;
  }
  .chat-line {
    position: absolute; left: 0; right: 0; top: 214px;
    font-family: "Anton", sans-serif; font-size: 44px; line-height: 64px;
    color: var(--ink);
  }

  .footer { position: absolute; left: 0; top: 351px; width: 702px; height: 849px; background: var(--espresso); color: var(--sand); }
  .brand-name {
    position: absolute; left: 0; right: 0; top: 78px; text-align: center;
    font-family: "Bebas Neue", sans-serif; font-weight: 400; font-size: 148px; line-height: 1; color: var(--sand);
  }
  .info-block { position: absolute; text-align: center; width: 330px; }
  .info-block.left { left: 11px; }
  .info-block.right { left: 332px; }
  .info-label { font-family: "Bebas Neue", sans-serif; font-size: 38px; line-height: 40px; }
  .info-text { font-family: "Oswald", sans-serif; font-weight: 300; font-size: 20px; line-height: 35px; }
  .copyright { font-family: "Bebas Neue", sans-serif; font-size: 40px; }
</style>
</head>
<body>
<div class="page">
  <section class="signup-band">
    <h2 class="signup-title">Let us contact you</h2>
    <div class="email-field">Please enter your email...</div>
    <div class="join-button">JOIN</div>
    <p class="chat-line">Contact Us on Chatline:<br>+555018842</p>
  </section>

  <footer class="footer">
    <h1 class="brand-name">VELMORA</h1>

    <div class="info-block left" style="top:304px">
      <div class="info-label">EMAIL</div>
      <div class="info-text">abc@velmail.example</div>
    </div>
    <div class="info-block left" style="top:426px">
      <div class="info-label">PHONE</div>
      <div class="info-text">+5550177</div>
    </div>
    <div class="info-block left" style="top:549px">
      <div class="info-label">SOCIAL</div>
      <div class="info-text">SNAPGRID<br>CIRCLEFEED<br>QUILL</div>
    </div>

    <div class="info-block right" style="top:304px">
      <div class="info-label">OFFICE</div>
      <div class="info-text">27 Harbour Lane W, Marwen City, Qasra –<br>41446, Solvane</div>
    </div>
    <div class="info-block right" style="top:462px">
      <div class="info-label">LEGAL</div>
      <div class="info-text">Privacy Policy<br>Terms of Service</div>
    </div>
    <div class="info-block right" style="top:614px">
      <div class="copyright">@2025-VELMORA</div>
    </div>
  </footer>
</div>
</body>
</html>
```